Land Buying Company Needs Letterhead for Direct Mail Marketing to Land Owners

We are looking for a professional letterhead that we will be including in our direct mail marketing. We will be sending this to land owners who may be interested in selling or purchasing land.

The letterhead needs to be editable. Headers and footers would look nice, but we are open. We would want it to include our address, website, phone, and email info. For right now the address to use for design purposes would the following:

Address: 415 Bramwell Avenue #600
Dallas, TX 75219
Website - www.quillridgeacres.example
Email - info@quillridgeacres.example
Phone - 866-402-ACRE

I have attached our logo zip file that we just had done on Pixel Guild. Let me know what questions you have, and thank you.

```html
<!DOCTYPE html>
<html lang="en">
<head>
<meta charset="utf-8">
<title>Quill Ridge Acres Letterhead</title>
<link rel="stylesheet" href="https://fonts.googleapis.com/css2?family=Open+Sans:wght@400;600&family=Lato:wght@400;700&display=swap">
<style>
  :root {
    --forest: #3f5e1f;
    --leaf: #8cc63f;
    --ink: #4a4a4a;
    --ink-dark: #333333;
    --mist: #efefea;
    --paper: #ffffff;
    --backdrop: #e6e6e6;
  }
  * { margin: 0; padding: 0; box-sizing: border-box; }
  html, body {
    width: 1040px; height: 1200px; overflow: hidden;
    background: var(--backdrop);
  }
  .letterhead {
    position: absolute; left: 70px; top: 20px;
    width: 900px; height: 1160px;
    background: var(--paper);
    box-shadow: 0 2px 10px rgba(0,0,0,0.12);
    overflow: hidden;
    font-family: "Open Sans", sans-serif;
    color: var(--ink);
  }
  .brand {
    position: absolute; top: 30px; left: 0; width: 100%;
    display: flex; justify-content: center; align-items: center; gap: 14px;
  }
  .brand-dot {
    width: 50px; height: 50px; border-radius: 50%;
    background: var(--forest);
  }
  .brand-name {
    font-family: "Open Sans", sans-serif;
    font-weight: 600; font-size: 34px; letter-spacing: 1px;
    color: var(--leaf); text-transform: uppercase;
  }
  .backdrop-disc {
    position: absolute; left: 202px; top: 305px;
    width: 524px; height: 524px; border-radius: 50%;
    background: var(--mist);
  }
  .letter-body {
    position: absolute; left: 84px; top: 342px; width: 728px;
    font-size: 14.5px; line-height: 26px;
    text-align: justify;
  }
  .letter-body p { margin-bottom: 26px; }
  .salutation { margin-bottom: 20px !important; }
  .signoff { position: absolute; left: 84px; top: 784px; font-size: 14.5px; }
  .signatory { position: absolute; left: 84px; top: 858px; }
  .signatory-name { font-size: 19px; font-weight: 600; color: var(--ink-dark); }
  .signatory-role { font-size: 14.5px; margin-top: 2px; }
  .footer-band {
    position: absolute; left: 0; bottom: 0; width: 100%; height: 76px;
    background: var(--forest);
    font-family: "Lato", sans-serif; color: #ffffff; font-size: 17px;
  }
  .footer-contact {
    position: absolute; left: 84px; top: 12px;
    width: 579px; padding-bottom: 3px;
    border-bottom: 1.5px solid #ffffff;
  }
  .footer-contact b { font-weight: 700; }
  .footer-address { position: absolute; left: 84px; top: 44px; }
</style>
</head>
<body>
  <main class="letterhead">
    <header class="brand">
      <span class="brand-dot"></span>
      <span class="brand-name">Quill Ridge Acres</span>
    </header>

    <div class="backdrop-disc" aria-hidden="true"></div>

    <section class="letter-body">
      <p class="salutation">Dear Mr.XYZABC</p>
      <p>Lorem Ipsum has been the industry's standard dummy text ever since the 1500s, when an unknown printer took a galley of type and scrambled it to make a type specimen book. It has survived not only five centuries, but also the leap into electronic typesetting, remaining essentially unchanged. It was popularised in the 1960s with the release of Letraset sheets containing Lorem Ipsum passages, and more recently with desktop publishing software like Aldus PageMaker including versions of Lorem Ipsum.</p>
      <p>Lorem Ipsum is simply dummy text of the printing and typesetting industry. Lorem Ipsum has been the industry's standard dummy text ever since the 1500s, when an unknown printer took a galley of type and scrambled it to make a type specimen book.</p>
      <p>It has survived not only five centuries, but also the leap into electronic typesetting, remaining essentially unchanged. It was popularised in the 1960s with the release of Letraset sheets containing Lorem IpsumIpsum passages.</p>
    </section>

    <p class="signoff">Yours Sincerely</p>
    <div class="signatory">
      <p class="signatory-name">Dorian Hale</p>
      <p class="signatory-role">Managing Director</p>
    </div>

    <footer class="footer-band">
      <p class="footer-contact"><b>P :</b> 866-402-ACRE &nbsp;| <b>E :</b> info@quillridgeacres.example</p>
      <p class="footer-address">www.quillridgeacres.example | 415 Bramwell Avenue #600 Dallas, TX 75219</p>
    </footer>
  </main>
</body>
</html>
```